Morvale Consulting Website Design

We have a great logo design and we want a great website to match. We are a business transformation consultancy that also provide learning and development in lean and transformation services

we use Lean as our core business transformnation approach.

We envisage the web being our key source of business, the website must be attractive to the target market, easy to use.

It should emulate our business which is making businesses easier to use as a customer, customer experience is a key value proposition for us.

Our proposition is...  'We deliver guaranteed bottom line results by re-designing companies based on how their value is really created…..and lost'

 

The format should be HTML and easily transferable to a web company for hosting.
Updates

The Website should ideally incorporate the following:

Basic functionality

• Contact Us Form (basic is fine) Contact Morvale About? i.e. (Job / Seeking Morvale's Services / Potential Supplier), Subject, Title, Full Name, Address, Post Code, Country, Email, Telephone number mobile/office, Fax, Free text for up to 1000 characters.
• Client Login Area - Username, Password
• Search Function
• Breadcrumb details
• Site Map
• Legal Notice
• Privacy Statement
• Sustainability
• Chirpline (link to )
• Blog
• RSS feed
Links to following content pages:
• About MORVALE
• Consulting
• Training
• Companies
• Careers
• Ideas

Links to following core products:

(text may read: Find out how we help organisations with...)

• Redefining Value
• Collections Readiness
• Equipping People
• Customer Experience

 

Thanks for the designs so far. We would like to direct designers back to the brief. We are expecting something that will appeal to CEO's, Snr mgt of major organisations. We are also expecting more than just a home page for the prize on offer. Appreciate the efforts so far. You can of course review other consulting company websites to assess competition and improve on. Kind regards Rolf

Target Market(s)

Major financial services, banking, major service organisations, blue chip,

Asia, Middle East,

CEO's, Senior  Management looking to transform the way their service companies do business

Industry/Entity Type

Consulting

Requirements
Must have
• Professional feel and image
• treat home page as a ''shop front'' for directing potential customers to the right information
• feeling of a large organisation
• Appeal to CEO''s, Senior Management of top flight oprganisations
• Consistent feel and usability
• Usability is extremely important as a key part of our product is simplifying busineses as an employee and a customer
• A home page and 2-3 other page styles for content
• Thought around branding on the home page, advertising board... that would not be used on content pages.
Nice to have
• A choice of colours, we dont mind considering different colour schemes. At least a few ideas for the use of black, white and reds as per existing logo design.
• Simple clean feel
•  Likely will have a large area for corporate branding using flash animation etc.
•  Weve been thinking through business tag lines susch as ''making the invisible, visible'', ''redefining busines value''
• Usable on a mobile device.
Should not have
• manufacturing feel
• a feeling of a small organisation
• many different areas that are confusing 
•  Lots of crazy flash work thats confusing to the eye.

```html
<!DOCTYPE html>
<html lang="en">
<head>
<meta charset="utf-8">
<title>Morvale Consulting</title>
<link rel="stylesheet" href="https://fonts.googleapis.com/css2?family=Arimo:wght@400;700&family=Tinos&display=swap">
<style>
:root{
  --brand-red:#a6213a;
  --heading-red:#c8283a;
  --ink:#111;
  --grey-text:#555;
  --panel-border:#d6d6d6;
  --panel-bg:#f4f4f4;
  --nav-top:#f6f6f6;
  --nav-bottom:#d9d9d9;
  --orange:#f07c0a;
  --green:#7cc21b;
  --link-blue:#1b3f8f;
  --footer-bg:#2f2f34;
  --white:#fff;
}
*{box-sizing:border-box;margin:0;padding:0}
html,body{width:1200px;height:1080px;overflow:hidden;background:var(--white)}
body{font-family:"Arimo",Arial,sans-serif;color:var(--ink);position:relative}
.abs{position:absolute}

/* header */
.brand{left:68px;top:60px;display:flex;align-items:center;gap:12px}
.brand-square{width:34px;height:34px;background:var(--brand-red)}
.brand-name{font-size:28px;color:var(--brand-red);font-weight:400;letter-spacing:.5px}

.login-icon{left:606px;top:40px;width:62px;height:62px;border-radius:50%;
  background:radial-gradient(circle at 40% 35%,#ffb04a,var(--orange) 70%);border:3px solid #e6e6e6}
.login-box{left:634px;top:24px;width:482px;height:96px;border:1px solid var(--panel-border);border-radius:6px}
.login-label{font-size:12px;color:#333;top:10px}
.login-label span{color:var(--orange)}
.login-input{top:32px;height:26px;border:1px solid #888;background:var(--white)}
.login-btn{left:411px;top:32px;width:60px;height:26px;background:linear-gradient(#9ad84a,var(--green));
  color:var(--white);font-size:14px;font-weight:700;display:flex;align-items:center;justify-content:center;border-radius:2px}
.login-link{top:64px;font-size:13px;color:var(--link-blue);text-decoration:underline}
.login-link::before{content:"»";text-decoration:none;display:inline-block;margin-right:3px;color:var(--link-blue)}

/* main nav */
.main-nav{left:68px;top:132px;width:1049px;height:50px;display:flex;border:1px solid #cfcfcf;border-radius:4px;
  background:linear-gradient(var(--nav-top),var(--nav-bottom));overflow:hidden}
.main-nav a{flex:1;display:flex;align-items:center;justify-content:center;font-size:16px;color:#555;
  text-decoration:none;border-right:1px solid #bcbcbc}
.main-nav a:last-child{border-right:0}

/* side panels */
.side-panel{border:1px solid var(--panel-border);border-radius:5px}
.side-nav{left:68px;top:196px;width:238px;height:428px;background:linear-gradient(var(--white),var(--panel-bg) 40%,#e9e9e9)}
.panel-title{font-size:17px;font-weight:400;color:var(--brand-red);letter-spacing:.3px}
.side-nav .panel-title{position:absolute;left:17px;top:16px}
.side-links{position:absolute;left:12px;top:46px;width:210px;list-style:none}
.side-links li{height:36px;display:flex;align-items:center;border-bottom:1px dotted #bbb;font-size:15px;color:#222;padding-left:16px}
.side-links li:last-child{border-bottom:0}
.side-links li::before{content:"»";margin-right:9px;font-size:13px}

.search-panel{left:66px;top:634px;width:240px;height:114px}
.search-panel .panel-title{position:absolute;left:13px;top:17px;color:var(--orange);font-weight:700;font-size:15px}
.search-label{position:absolute;left:14px;top:50px;font-size:12px;font-weight:700;color:#444}
.search-input{position:absolute;left:13px;top:66px;width:140px;height:24px;border:1px solid #999;background:var(--white)}
.search-btn{position:absolute;left:157px;top:66px;width:58px;height:24px;background:#666;color:var(--white);
  font-size:14px;font-weight:700;display:flex;align-items:center;justify-content:center}

.media{background:linear-gradient(135deg,#d5d5d5,#8d8d93)}
.globe-art{left:58px;top:756px;width:234px;height:218px;background:radial-gradient(ellipse at 60% 60%,#e4b94a,#b88a24 55%,#fff 72%)}

/* hero */
.hero-photo{left:331px;top:191px;width:454px;height:212px;background:linear-gradient(110deg,#5a5a62,#2c2c33 50%,#8b8b92)}
.hero-copy{left:808px;top:196px}
.hero-title{font-size:21px;color:var(--heading-red);line-height:27px;letter-spacing:.2px}
.hero-sub{margin-top:12px;font-size:14px;font-weight:700;color:#555;letter-spacing:.3px}
.hero-list{margin-top:20px;list-style:none;font-size:15px;line-height:19px}
.hero-list li::before{content:"* ";}

/* articles */
.post-icon{width:53px;height:53px;border-radius:50%;background:radial-gradient(circle at 40% 35%,#6aa9ef,#1c5fb8 70%);
  border:3px solid #d9e3ef;display:flex;align-items:center;justify-content:center}
.post-title{font-size:16px;font-weight:700;font-size:15.5px}
.post-body{font-size:14px;line-height:15.4px;color:var(--ink);width:796px}
.dash-rule{height:0;border-top:1px dashed #555;width:790px}
.post-links{font-size:14px;font-weight:700;color:#444;display:flex;gap:20px}
.post-links a{color:#444;text-decoration:underline}
.post-links span::before{content:"» ";font-weight:400}

.gallery{left:325px;top:746px;width:792px;height:131px;border:2px solid #ececec;border-radius:8px;box-shadow:0 1px 3px #ccc}
.thumb{position:absolute;top:8px;width:182px;height:112px;border:1px solid #ccc}

/* footer */
.site-footer{left:61px;top:1012px;width:1059px;height:68px;background:var(--footer-bg);color:var(--white);text-align:center}
.footer-links{font-family:"Tinos","Times New Roman",serif;font-size:13.5px;margin-top:14px}
.footer-links span{margin:0 10px}
.footer-copy{font-size:14.5px;margin-top:6px}
.footer-copy b{font-weight:400;margin-left:20px}
</style>
</head>
<body>

<header>
  <div class="abs brand">
    <div class="brand-square"></div>
    <div class="brand-name">MORVALE CONSULTING</div>
  </div>

  <div class="abs login-box">
    <div class="abs login-label" style="left:45px">Username: <span>*</span></div>
    <div class="abs login-label" style="left:230px">Password: <span>*</span></div>
    <div class="abs login-input" style="left:45px;width:175px"></div>
    <div class="abs login-input" style="left:230px;width:175px"></div>
    <div class="abs login-btn">Login</div>
    <a class="abs login-link" style="left:45px">Create new account</a>
    <a class="abs login-link" style="left:195px">Lost password?</a>
  </div>
  <div class="abs login-icon">
    <svg width="56" height="56" viewBox="0 0 56 56" aria-hidden="true">
      <circle cx="28" cy="21" r="6" fill="#fff"/>
      <path d="M19 40 q0-11 9-11 q9 0 9 11 z" fill="#fff"/>
    </svg>
  </div>

  <nav class="abs main-nav">
    <a>Home</a><a>About Morvale</a><a>Consulting</a><a>Training</a><a>Companies</a><a>Careers</a><a>Ideas</a>
  </nav>
</header>

<aside>
  <div class="abs side-panel side-nav">
    <h2 class="panel-title">NAVIGATION</h2>
    <ul class="side-links">
      <li>Home</li><li>Breadcrumb Details</li><li>Site Map</li><li>Blog</li><li>Legal Notice</li>
      <li>Sustainability</li><li>Chirpline (link to )</li><li>FAQ's</li><li>Contact Us</li><li>RSS feed</li>
    </ul>
  </div>
  <div class="abs side-panel search-panel">
    <h2 class="panel-title">SEARCH</h2>
    <div class="search-label">Search this site:</div>
    <div class="search-input"></div>
    <div class="search-btn">Search</div>
  </div>
  <div class="abs globe-art" role="img" aria-label="Gold figure with a laptop sitting on a globe beside large WWW letters"></div>
</aside>

<main>
  <div class="abs hero-photo" role="img" aria-label="Group of business people in dark suits"></div>
  <div class="abs hero-copy">
    <div class="hero-title">FIND OUT HOW WE HELP<br>ORGANISATIONS WITH...</div>
    <div class="hero-sub">CONDUCTING HONEST BUSINESS!</div>
    <ul class="hero-list">
      <li>&nbsp;Redefining Value</li><li>Collections Readiness</li><li>Equipping People</li><li>Customer Experience</li>
    </ul>
  </div>

  <div class="abs post-icon" style="left:326px;top:408px">
    <svg width="28" height="26" viewBox="0 0 28 26" aria-hidden="true"><rect x="2" y="2" width="24" height="16" rx="2" fill="#fff"/><rect x="11" y="18" width="6" height="4" fill="#fff"/><rect x="7" y="22" width="14" height="2" fill="#fff"/></svg>
  </div>
  <div class="abs post-title" style="left:395px;top:424px">Lorem ipsum dolor sit amet, consectetur</div>
  <p class="abs post-body" style="left:328px;top:467px">Lorem ipsum dolor sit amet, consectetur adipiscing&nbsp; Aenean at ipsum. Sed pretium auctor massa. Cum sociis lorem natoque penatibus et magnis disparturient montes, nascetur ridiculus mus. Curabitur euismod.. Lorem sit amet and Lorem ipsum dolor sit amet, consectetur adipiscing&nbsp; Aenean at ipsum. Sed pretium auctor massa. Cum sociis lorem natoque penatibus et magnis disparturient montes, nascetur ridiculus mus. Curabitur euismod.. Lorem sit amet and Lorem ipsum dolor sit amet, consectetur adipiscing&nbsp; Aenean at ipsum. Sed pretium auctor massa. Cum sociis lorem natoque penatibus et magnis disparturient montes, nascetur ridiculus mus. Curabitur euismod.. Lorem sit amet and Lorem ipsum dolor sit amet, consectetur adipiscing&nbsp; Aenean at ipsum. Sed pretium auctor massa. Cum sociis lorem natoque penatibus et magnis disparturient montes, nascetur ridiculus mus. Curabitur euismod.. Lorem sit amet and</p>
  <div class="abs dash-rule" style="left:330px;top:599px"></div>
  <div class="abs post-links" style="left:338px;top:616px"><span><a>admin's blog</a></span><span><a>Read more</a></span></div>

  <div class="abs post-icon" style="left:326px;top:641px">
    <svg width="28" height="26" viewBox="0 0 28 26" aria-hidden="true"><rect x="2" y="2" width="24" height="16" rx="2" fill="#fff"/><rect x="11" y="18" width="6" height="4" fill="#fff"/><rect x="7" y="22" width="14" height="2" fill="#fff"/></svg>
  </div>
  <div class="abs post-title" style="left:395px;top:652px">Lorem ipsum dolor sit amet, consectetur</div>
  <p class="abs post-body" style="left:328px;top:693px">Lorem ipsum dolor sit amet, consectetur adipiscing elit. Aenean at ipsum. Sed pretium auctor massa. Cum sociis natoque penatibus et magnis disparturient montes, nascetur ridiculus mus. Curabitur euismod.</p>

  <div class="abs gallery">
    <div class="thumb media" style="left:10px;background:linear-gradient(135deg,#4a3a3a,#c9b5b5)" role="img" aria-label="Hands holding a piggy bank"></div>
    <div class="thumb media" style="left:203px;background:linear-gradient(135deg,#9bb0c4,#e7ddd2)" role="img" aria-label="Colleagues reviewing papers in an office"></div>
    <div class="thumb media" style="left:399px;background:linear-gradient(135deg,#f2f2f2,#b9b0a6)" role="img" aria-label="Team meeting around a table"></div>
    <div class="thumb media" style="left:595px;background:linear-gradient(135deg,#e5e5ea,#6d5f7a)" role="img" aria-label="Two women working at a computer"></div>
  </div>
  <p class="abs post-body" style="left:332px;top:887px;width:780px;line-height:16.5px">Lorem ipsum dolor sit amet, consectetur adipiscing&nbsp; Aenean at ipsum. Sed pretium auctor massa. Cum sociis natoque penatibus et magnis disparturient montes, nascetur ridiculus mus. Curabitur euismod tortor id metus. Curabitur eget quam vitae leo malesuada adipiscing.</p>
  <div class="abs dash-rule" style="left:330px;top:943px"></div>
  <div class="abs post-links" style="left:334px;top:960px"><span><a>admin's blog</a></span><span><a>Read more</a></span></div>
</main>

<footer class="abs site-footer">
  <div class="footer-links"><span>Site Map</span>|<span>Legal Notice</span>|<span>Privacy Statement</span></div>
  <div class="footer-copy">Copyright @ Your Company Name All rights reserved <b>Terms of Use</b>&nbsp; | &nbsp;Privacy Policy</div>
</footer>

</body>
</html>
```